DIGITAL MENUS

Hi Odette (This project is for Odette ONLY)Hope you are well. Can you please help me with designing a new menu for me.I've attached my current menu for you. I would like a new layout using photos for each items.You can use same photos as the menu board that you have designed for me before.Layout must be in Landscape form as current menu. JPEG files.

Need extra days to review

• Hi Odette,
• Ideal layout:
• DISPLAY MENU #1:
• Rice paper Rolls and Spring rolls
• Pho
• DISPLAY MENU #2:
• Noodle Salads
• Rice
• Stirfry Noodles
• DISPLAY MENU #3:
• Drinks
• 1. All soft drinks $3
• 2. Cape Harrowby water $3
• 3. T. Varsenzo Sparkling water $4.5
• 4. Zestora Water $4.5
• 5. Harbek Ice-Tea $4.5
• 6. Pulpwell Juices $5
• 7. Kombucha $5
• and Vietnamese Drinks

```html
<!DOCTYPE html>
<html lang="en">
<head>
<meta charset="utf-8">
<title>Digital Menu Boards</title>
<link rel="stylesheet" href="https://fonts.googleapis.com/css2?family=Bebas+Neue&family=Roboto:wght@700&display=swap">
<style>
:root{
  --page:#ffffff;
  --board-light:#f4f4f3;
  --board-mid:#e9e9e8;
  --orange:#f26522;
  --ink:#1c1c1c;
  --muted:#555555;
  --pill-black:#0e0e0e;
  --white:#ffffff;
}
*{margin:0;padding:0;box-sizing:border-box}
html,body{width:1200px;height:1200px;overflow:hidden;background:var(--page)}
body{position:relative;font-family:"Roboto",Arial,sans-serif;font-weight:700;color:var(--ink)}
.board{position:absolute;left:273px;width:660px;height:370px;
  background:linear-gradient(135deg,var(--board-light) 0%,var(--board-mid) 45%,var(--board-light) 70%,var(--board-mid) 100%);overflow:hidden}
.board--starters{top:31px}
.board--mains{top:419px}
.board--drinks{top:808px}
.section-title{position:absolute;left:32px;font-family:"Bebas Neue",Impact,sans-serif;color:var(--orange);font-size:29px;line-height:24px;font-weight:400}
.section-price{position:absolute;left:32px;font-family:"Bebas Neue",Impact,sans-serif;color:var(--ink);font-size:25px;line-height:22px;font-weight:400}
.rule{position:absolute;left:30px;height:2px;background:var(--orange)}
.photo{position:absolute;border-radius:14px}
.photo--plate{background:radial-gradient(ellipse at 50% 55%,#d8b48a 0%,#e9dccb 38%,#fafafa 62%,rgba(250,250,250,0) 75%)}
.photo--bowl{background:radial-gradient(ellipse at 50% 45%,#9a6a3e 0%,#c9a36d 30%,#eef2f3 58%,rgba(240,240,240,0) 74%)}
.photo--greens{background:radial-gradient(ellipse at 50% 50%,#7a4a2c 0%,#5e8a3a 28%,#e07a3a 42%,#f7f7f7 62%,rgba(247,247,247,0) 76%)}
.photo--pho{border-radius:50%;background:radial-gradient(ellipse at 55% 50%,#6b3a1d 0%,#8a5a2e 30%,#4e7a38 45%,#f5f5f5 66%,rgba(245,245,245,0) 78%)}
.photo--drinks{border-radius:18px;background:linear-gradient(90deg,rgba(160,200,90,.55) 0%,rgba(240,215,120,.6) 35%,rgba(210,40,40,.55) 62%,rgba(60,170,90,.5) 82%,rgba(240,240,240,0) 100%)}
.label{position:absolute;text-align:center;font-size:11.5px;line-height:11.5px;text-transform:uppercase;white-space:nowrap;transform:translateX(-50%)}
.label small{display:block;font-size:11.5px;line-height:11.5px}
.label .note{display:block;color:var(--muted);text-transform:none;font-size:12.5px;line-height:14px;margin-top:2px}
.price{position:absolute;font-family:"Bebas Neue",Impact,sans-serif;font-weight:400;font-size:23px;line-height:20px;text-align:center;transform:translateX(-50%);white-space:nowrap}
.price small{display:block;font-family:"Roboto",Arial,sans-serif;font-weight:700;font-size:10.5px;line-height:10px}
.price-pair{position:absolute;display:flex;gap:20px;transform:translateX(-50%)}
.price-pair .price{position:static;transform:none}
.menu-list{position:absolute;list-style:none;font-size:11.5px;text-transform:uppercase}
.menu-list li{line-height:16.7px;white-space:nowrap}
.menu-list .sub{display:block;line-height:10.6px;margin-top:-3px;margin-bottom:3.2px;padding-left:20px;font-weight:400;-webkit-text-stroke:.25px var(--ink)}
.menu-list .num{display:inline-block;min-width:14px;text-align:right;margin-right:5px}
.extras{position:absolute;width:291px;height:33px;border-radius:17px;background:var(--orange);display:flex;overflow:hidden;color:var(--white)}
.extras__head{width:58px;background:var(--pill-black);border-radius:17px 0 0 17px;font-family:"Bebas Neue",Impact,sans-serif;font-weight:400;font-size:15px;line-height:13px;display:flex;flex-direction:column;justify-content:center;align-items:center;padding-left:4px}
.extras__item{display:flex;flex-direction:column;align-items:center;justify-content:center;padding:0 6px}
.extras__item b{font-family:"Bebas Neue",Impact,sans-serif;font-weight:400;font-size:16px;line-height:14px;color:#ffe1cf}
.extras__item span{font-size:9.5px;line-height:10px}
.drinks-list{position:absolute;list-style:none;font-size:11.5px;text-transform:uppercase}
.drinks-list li{display:flex;justify-content:space-between;line-height:16.7px;width:286px;white-space:nowrap}
.drinks-list li b{font-family:"Bebas Neue",Impact,sans-serif;font-weight:400;font-size:15px}
.viet-list{position:absolute;list-style:none;font-size:11.5px;text-transform:uppercase}
.viet-list li{line-height:19.4px;white-space:nowrap}
.viet-list .num{display:inline-block;min-width:14px;text-align:right;margin-right:5px}
</style>
</head>
<body>

<!-- Board 1: Rolls and Pho -->
<section class="board board--starters">
  <h2 class="section-title" style="top:24px">Rolls</h2>

  <div class="photo photo--plate" style="left:111px;top:19px;width:119px;height:69px" role="img" aria-label="Rice paper rolls on a white plate"></div>
  <div class="photo photo--plate" style="left:280px;top:19px;width:112px;height:69px" role="img" aria-label="Spring rolls with chilli dipping sauce"></div>
  <div class="photo photo--plate" style="left:446px;top:19px;width:112px;height:69px" role="img" aria-label="Potato shrimp with chilli dipping sauce"></div>

  <div class="label" style="left:166px;top:93px">Ricepaper Rolls</div>
  <div class="price-pair" style="left:166px;top:110px">
    <div class="price">$7.00<small>2 Rolls</small></div>
    <div class="price">$10.00<small>3 Rolls</small></div>
  </div>

  <div class="label" style="left:337px;top:93px">Spring Rolls (4)<span class="note">(Seafood/Vegetarian)</span></div>
  <div class="price" style="left:337px;top:121px">$7.00</div>

  <div class="label" style="left:503px;top:93px">Potato Shrimp (4)</div>
  <div class="price" style="left:503px;top:109px">$7.00</div>

  <div class="rule" style="top:148px;width:600px"></div>

  <h2 class="section-title" style="top:160px">Phở</h2>
  <div class="section-price" style="top:184px">$13.50</div>

  <ol class="menu-list" style="left:106px;top:153px">
    <li><span class="num">1.</span>Rare Beef</li>
    <li><span class="num">2.</span>Cooked Beef</li>
    <li><span class="num">3.</span>Rare + Cooked Beef</li>
    <li><span class="num">4.</span>Beef Balls</li>
    <li><span class="num">5.</span>Rare + Beef Balls</li>
    <li><span class="num">6.</span>Cooked + Beef Balls</li>
    <li><span class="num">7.</span>Chicken</li>
    <li><span class="num">8.</span>Beef + Chicken<span class="sub">(Rare/Cooked Beef + Chicken)</span></li>
    <li><span class="num">9.</span>Combination<span class="sub">Rare + Cooked + Beef Balls</span></li>
    <li><span class="num">10.</span>Tofu<span class="sub">(With Vegetarian/Beef Stock)</span></li>
  </ol>

  <div class="photo photo--pho" style="left:315px;top:159px;width:309px;height:159px" role="img" aria-label="Three bowls of pho with herbs, onion and tofu"></div>

  <div class="extras" style="left:328px;top:319px">
    <div class="extras__head">*Add<br>Extra</div>
    <div class="extras__item"><b>$2.00</b><span>MEAT</span></div>
    <div class="extras__item"><b>$2.00</b><span>VEGETABLES</span></div>
    <div class="extras__item"><b>$2.00</b><span>TOFU</span></div>
    <div class="extras__item"><b>$1.50</b><span>NOODLES</span></div>
  </div>
</section>

<!-- Board 2: Noodle salad, stirfry noodles, rice -->
<section class="board board--mains">
  <h2 class="section-title" style="top:18px">Noodle<br>Salad</h2>
  <div class="section-price" style="top:72px">$13.50</div>

  <div class="photo photo--bowl" style="left:139px;top:15px;width:106px;height:72px" role="img" aria-label="Lemongrass beef noodle salad"></div>
  <div class="photo photo--bowl" style="left:268px;top:15px;width:106px;height:72px" role="img" aria-label="Lemongrass chicken noodle salad"></div>
  <div class="photo photo--bowl" style="left:392px;top:15px;width:106px;height:72px" role="img" aria-label="BBQ pork noodle salad"></div>
  <div class="photo photo--bowl" style="left:518px;top:15px;width:106px;height:72px" role="img" aria-label="Tofu noodle salad"></div>

  <div class="label" style="left:192px;top:90px">1. Lemongrass<small>Beef</small></div>
  <div class="label" style="left:319px;top:90px">2. Lemongrass<small>Chicken</small></div>
  <div class="label" style="left:447px;top:90px">3. BBQ Pork</div>
  <div class="label" style="left:570px;top:90px">4. Tofu</div>

  <div class="rule" style="top:115px;width:600px"></div>

  <h2 class="section-title" style="top:120px">Stirfry<br>Noodles</h2>
  <div class="section-price" style="top:175px">$15.50</div>

  <div class="photo photo--greens" style="left:186px;top:122px;width:116px;height:69px" role="img" aria-label="Beef stirfry noodles with vegetables"></div>
  <div class="photo photo--greens" style="left:311px;top:122px;width:116px;height:69px" role="img" aria-label="Chicken stirfry noodles with vegetables"></div>
  <div class="photo photo--greens" style="left:436px;top:122px;width:116px;height:69px" role="img" aria-label="Tofu stirfry noodles with vegetables"></div>

  <div class="label" style="left:244px;top:200px">1. Beef</div>
  <div class="label" style="left:369px;top:200px">2. Chicken</div>
  <div class="label" style="left:494px;top:200px">3. Tofu</div>

  <div class="rule" style="top:213px;width:600px"></div>

  <h2 class="section-title" style="top:223px">Rice</h2>
  <div class="section-price" style="top:250px">$15.50</div>

  <div class="photo photo--greens" style="left:109px;top:219px;width:115px;height:69px" role="img" aria-label="BBQ beef with rice and broccoli"></div>
  <div class="photo photo--greens" style="left:236px;top:219px;width:115px;height:69px" role="img" aria-label="Lemongrass chilli chicken with rice"></div>
  <div class="photo photo--greens" style="left:364px;top:219px;width:115px;height:69px" role="img" aria-label="Tofu and vegetables with rice"></div>
  <div class="photo photo--plate" style="left:486px;top:219px;width:115px;height:69px" role="img" aria-label="Fried rice with prawns"></div>

  <div class="label" style="left:169px;top:294px">1. BBQ Beef</div>
  <div class="label" style="left:296px;top:294px">2. Lemongrass<small>Chilli Chicken</small></div>
  <div class="label" style="left:421px;top:294px">3. Tofu &amp; Vegs</div>
  <div class="label" style="left:545px;top:294px">4. Fried Rice<span class="note">(Prawns/Chicken/Tofu)</span></div>

  <div class="extras" style="left:184px;top:320px">
    <div class="extras__head">*Add<br>Extra</div>
    <div class="extras__item"><b>$2.00</b><span>MEAT</span></div>
    <div class="extras__item"><b>$2.00</b><span>VEGETABLES</span></div>
    <div class="extras__item"><b>$2.00</b><span>TOFU</span></div>
    <div class="extras__item"><b>$1.50</b><span>NOODLES</span></div>
  </div>
</section>

<!-- Board 3: Drinks -->
<section class="board board--drinks">
  <h2 class="section-title" style="top:47px;left:34px">Drinks</h2>

  <ol class="drinks-list" style="left:174px;top:44px">
    <li><span>1. All Softdrinks</span><b>$3.00</b></li>
    <li><span>2. Cape Harrowby Water</span><b>$3.00</b></li>
    <li><span>3. T. Varsenzo Sparkling Water</span><b>$4.50</b></li>
    <li><span>4. Zestora Water</span><b>$4.50</b></li>
    <li><span>5. Harbek Ice-Tea</span><b>$4.50</b></li>
    <li><span>6. Pulpwell Juices</span><b>$5.00</b></li>
    <li><span>7. Kombucha</span><b>$5.00</b></li>
  </ol>

  <div class="rule" style="top:166px;width:433px"></div>

  <h2 class="section-title" style="top:176px;left:34px">Vietnamese<br>Drinks</h2>
  <div class="section-price" style="top:230px;left:34px">$6.50</div>

  <ol class="viet-list" style="left:164px;top:174px">
    <li><span class="num">8.</span>Vietnamese Iced Coffee</li>
    <li><span class="num">9.</span>Vietnamese Fresh Lemon Soda</li>
    <li><span class="num">10.</span>Coconut Water</li>
    <li><span class="num">11.</span>Avocado Smoothie (Seasonal)</li>
    <li><span class="num">12.</span>Custard Apple Smoothie</li>
    <li><span class="num">13.</span>Durian Smoothie</li>
    <li><span class="num">14.</span>Lychee Smoothie</li>
    <li><span class="num">15.</span>Jackfruit Smoothie</li>
  </ol>

  <div class="photo photo--drinks" style="left:412px;top:178px;width:206px;height:172px" role="img" aria-label="Smoothies, bottled water, sparkling water and a soft drink can"></div>
</section>

</body>
</html>
```